Summit Grading a Builders LLC business card

My current business card is very plain. it has my logo and contact information. I woud like something that stands out from the rest. please take a look at my website to see about my company.

Compayt Name - Summit Grading And Builders
Owner - Martin Kowalczyk
Business Address
Business Website - www.summitgradingandbuilders.example
Email - Summitgradingandbuilders@mailbox.example
Phone - 555-214-7390
Fax - 555-806-3127

Target Market(s)

Everyone age tang is 18 - 85

Industry/Entity Type

Business

Contact Information for Business Card

Nice and professional all in one.

Font styles to use
Serif
Other font styles liked:
• Up to you

Requirements
Must have
• All contact info. The design is up to you.
Nice to have
• All the contact info the design is up to you
Should not have
• I don't have any

```html
<!DOCTYPE html>
<html lang="en">
<head>
<meta charset="utf-8">
<title>Summit Grading &amp; Builders LLC – Business Card</title>
<link rel="stylesheet" href="https://fonts.googleapis.com/css2?family=Exo+2:wght@700&family=Open+Sans:wght@400;600;700&display=swap">
<style>
  :root {
    --page: #e4e4e4;
    --card-dark: #2f2f2f;
    --map-tone: #3b3b3b;
    --card-light: #ffffff;
    --logo-light: #d6d6d6;
    --ink: #2a2a2a;
    --accent: #f0901e;
    --badge: #8a8a8a;
    --rule: #333333;
  }
  * { box-sizing: border-box; margin: 0; padding: 0; }
  html, body { width: 1200px; height: 1000px; overflow: hidden; }
  body {
    background: var(--page);
    font-family: "Open Sans", Arial, sans-serif;
    display: flex;
    flex-direction: column;
    align-items: center;
    justify-content: center;
    gap: 34px;
  }
  .card {
    position: relative;
    width: 800px;
    height: 457px;
    box-shadow: 0 6px 18px rgba(0,0,0,.18);
    overflow: hidden;
  }

  /* Front */
  .card--front { background: var(--card-dark); }
  .state-map {
    position: absolute;
    left: 250px; top: 40px;
    width: 360px; height: 300px;
    background: var(--map-tone);
    border-radius: 40px 90px 30px 60px;
  }
  .front-logo {
    position: absolute;
    left: 0; right: 0; top: 150px;
    text-align: center;
    color: var(--logo-light);
    font-weight: 700;
    font-size: 46px;
    line-height: 1.1;
    letter-spacing: 1px;
    text-transform: uppercase;
  }
  .front-web {
    position: absolute;
    left: 0; right: 0; bottom: 46px;
    text-align: center;
    color: #ffffff;
    font-size: 19px;
    letter-spacing: 1px;
  }
  .front-web .domain { color: var(--accent); }

  /* Back */
  .card--back { background: var(--card-light); color: var(--ink); }
  .back-logo {
    position: absolute;
    left: 44px; top: 34px;
    font-weight: 700;
    font-size: 26px;
    line-height: 1.1;
    color: var(--ink);
    text-transform: uppercase;
    letter-spacing: .5px;
  }
  .owner-name {
    position: absolute;
    left: 44px; top: 126px;
    font-family: "Exo 2", "Open Sans", sans-serif;
    font-weight: 700;
    font-size: 27px;
    letter-spacing: .5px;
    text-transform: uppercase;
  }
  .owner-title {
    position: absolute;
    left: 44px; top: 162px;
    width: 712px;
    font-size: 20px;
    color: var(--accent);
    display: flex;
    align-items: flex-end;
    gap: 2px;
  }
  .owner-title .rule {
    flex: 1;
    border-bottom: 1.5px solid var(--rule);
    margin-bottom: 4px;
  }
  .badges {
    position: absolute;
    left: 48px; top: 212px;
    display: flex; gap: 14px;
  }
  .badge { width: 46px; height: 46px; background: var(--badge); }
  .badge--round { border-radius: 50%; }
  .badge--square { border-radius: 6px; }
  .contacts {
    position: absolute;
    left: 48px; top: 288px;
    list-style: none;
    font-size: 19px;
    line-height: 29px;
  }
  .contacts li { display: flex; align-items: center; gap: 12px; }
  .contacts svg { width: 18px; height: 18px; fill: var(--accent); flex: none; }
  .address {
    position: absolute;
    right: 46px; bottom: 40px;
    text-align: right;
    font-size: 18px;
    line-height: 26px;
  }
</style>
</head>
<body>

<section class="card card--front" aria-label="Business card front">
  <div class="state-map" role="img" aria-label="Faint outline map of New York State"></div>
  <h1 class="front-logo">Summit Grading<br>&amp; Builders LLC</h1>
  <p class="front-web">www.<span class="domain">summitgradingandbuilders</span>.example</p>
</section>

<section class="card card--back" aria-label="Business card back">
  <p class="back-logo">Summit Grading<br>&amp; Builders LLC</p>
  <h2 class="owner-name">Martin Kowalczyk</h2>
  <p class="owner-title"><span>Owner</span><span class="rule"></span></p>
  <div class="badges">
    <span class="badge badge--round" role="img" aria-label="Partner badge"></span>
    <span class="badge badge--square" role="img" aria-label="Rating badge"></span>
  </div>
  <ul class="contacts">
    <li>
      <svg viewBox="0 0 24 24" aria-hidden="true"><path d="M6.6 10.8a15 15 0 0 0 6.6 6.6l2.2-2.2a1 1 0 0 1 1-.25 11.4 11.4 0 0 0 3.6.57 1 1 0 0 1 1 1V20a1 1 0 0 1-1 1A17 17 0 0 1 3 4a1 1 0 0 1 1-1h3.5a1 1 0 0 1 1 1c0 1.25.2 2.45.57 3.57a1 1 0 0 1-.25 1z"/></svg>
      555 214 7390
    </li>
    <li>
      <svg viewBox="0 0 24 24" aria-hidden="true"><path d="M7 3h10v5H7zM4 9h16a2 2 0 0 1 2 2v6h-4v4H6v-4H2v-6a2 2 0 0 1 2-2zm4 7v3h8v-3z"/></svg>
      555 806 3127
    </li>
    <li>
      <svg viewBox="0 0 24 24" aria-hidden="true"><path d="M2 5h20v14H2zm2 2v.5l8 5 8-5V7l-8 5z"/></svg>
      summitgradingandbuilders@mailbox.example
    </li>
    <li>
      <svg viewBox="0 0 24 24" aria-hidden="true"><path d="M12 2a10 10 0 1 0 0 20 10 10 0 0 0 0-20zm-1 2.1V8H7.6A8 8 0 0 1 11 4.1zm2 0A8 8 0 0 1 16.4 8H13zM4.3 10H11v4H4.3a8 8 0 0 1 0-4zm8.7 0h6.7a8 8 0 0 1 0 4H13zm-5.4 6H11v3.9A8 8 0 0 1 7.6 16zm5.4 0h3.4a8 8 0 0 1-3.4 3.9z"/></svg>
      www.summitgradingandbuilders.example
    </li>
  </ul>
  <p class="address">480 Elm Avenue, Riverton,<br>NY, United States</p>
</section>

</body>
</html>
```